Kiswa Design

We need a flyer design for a product that we are a selling, a sacred Islamic cloth called a Kiswah, which is draped around the holy Kaaba in mecca every year.

The details we would like on the flyer are as follows:

Rare Kiswah of the holy Kaaba for sale (fitted in 1977 and 1982 vintage). For sale:

1) whole piece 15 meters x 2.60 meters : £60,000
2) 8 meters x 2.60 meters : £31,200
3) 4 meters x 2.60 meters : £15,600
4) 1 meter : £1500

(insert a high quality picture of holy Kaaba here, then underneath the picture, write the following:) "The Kaaba is covered by an expensive black cloth which is known as 'Kiswah' which is produced and changed every year"

(insert picture of our product here,i.e. use the document named MAIN IMAGE then underneath this picture write the following:) "Silk lampas weave Kiswah, woven silk on a black satin ground with Quranic calligraphy, the zig-zag bands of inscription alternate with the Shahadah and the inscription, 'God, exalted be His Glory!"

insert another picture of kiswah which i provided anywhere you like

(somewhere on flyer write the following) please note a percentage of sales will go towards Sadaqah for our Muslim brothers and sisters in need around the world

(somewhere on flyer write the following) Hallorand's international auction house authenticity document also available to prove the Kiswah is genuine.

100% genuine

contact us today! deals this good don't last forever.

email: relicoffer@tarnwickmail.com

Please use the images that I have attached on the flyer accordingly. Also feel free to be as creative as possible I want it to attract a lot of attention but also look professional so you may add some things to improve the look of the flyer.

note: the product being sold is on the pictures I've provided, in particular, i want file 2 "main image" in a large size on the flyer!

thank you! and happy holidays

Muslims and Islamic collectors

House

• the dimensions of the flyer is :
• A5 horizontal or vertical
• (210 x 148 mm)
• must have colors! up to you what colors to choose!

```html
<!DOCTYPE html>
<html lang="en">
<head>
<meta charset="utf-8">
<title>Rare Kiswah of the Holy Kaaba – For Sale</title>
<link rel="stylesheet" href="https://fonts.googleapis.com/css2?family=Archivo+Black&family=Open+Sans:wght@400;600&family=PT+Sans:wght@400;700&family=Roboto+Condensed:wght@400;700&family=Rye&display=swap">
<style>
  :root {
    --ink: #000000;
    --white: #ffffff;
    --yellow: #f4e800;
    --price-yellow: #ffe500;
    --red: #e3161d;
    --gold-light: #f3d98a;
    --gold-mid: #c9a24a;
    --gold-dark: #7a5a1c;
    --olive: #8b8a3b;
    --green: #1b6a33;
  }
  * { margin: 0; padding: 0; box-sizing: border-box; }
  html, body { width: 847px; height: 1200px; overflow: hidden; background: var(--ink); }
  .flyer { position: relative; width: 847px; height: 1200px; background: var(--ink); overflow: hidden; font-family: "PT Sans", sans-serif; color: var(--white); }
  .shapes { position: absolute; inset: 0; }
  .txt { position: absolute; }
  .kaaba-quote {
    top: 10px; right: 28px; width: 270px; text-align: right;
    font-family: "Roboto Condensed", sans-serif; font-size: 15.5px; line-height: 17px; color: var(--yellow);
  }
  .cloth-caption {
    top: 456px; left: 530px; width: 294px; text-align: justify;
    font-family: "Open Sans", sans-serif; font-size: 13.6px; line-height: 20px; color: var(--white);
  }
  .rare { top: 598px; left: 272px; font-weight: 700; font-size: 41px; }
  .product-name {
    top: 640px; left: 0; width: 847px; text-align: center;
    font-family: "Rye", serif; font-size: 92px; line-height: 110px; letter-spacing: 2px;
    background: linear-gradient(180deg, var(--gold-light) 0%, var(--gold-mid) 45%, var(--gold-dark) 70%, var(--gold-light) 100%);
    -webkit-background-clip: text; background-clip: text; color: transparent;
  }
  .product-sub { top: 742px; left: 0; width: 847px; text-align: center; font-size: 45px; line-height: 52px; }
  .product-years { top: 792px; left: 0; width: 847px; text-align: center; font-size: 29px; line-height: 36px; }
  .for-sale {
    top: 832px; left: 0; width: 847px; text-align: center;
    font-family: "Archivo Black", sans-serif; font-size: 70px; line-height: 84px; letter-spacing: 5px; color: var(--red);
  }
  .price-list {
    top: 914px; left: 160px; list-style: none;
    font-family: "Roboto Condensed", sans-serif; font-weight: 700; font-size: 22.5px; line-height: 32.5px; color: var(--price-yellow); text-align: center;
  }
  .cta { top: 1058px; left: 0; width: 847px; text-align: center; font-family: "Open Sans", sans-serif; font-size: 18px; line-height: 25px; }
  .email { top: 1108px; left: 0; width: 847px; text-align: center; font-family: "Roboto Condensed", sans-serif; font-weight: 700; font-size: 30px; }
  .charity-note { top: 1003px; left: 18px; width: 200px; text-align: center; font-size: 17px; line-height: 21px; }
  .auth-note { top: 950px; left: 642px; width: 180px; text-align: center; font-size: 17px; line-height: 21px; }
  .seal-text {
    top: 781px; left: 44px; width: 126px; text-align: center; transform: rotate(-18deg);
    font-family: "Archivo Black", sans-serif; color: var(--white); line-height: 1;
  }
  .seal-text .big { font-size: 32px; display: block; }
  .seal-text .small { font-size: 20px; display: block; font-family: "PT Sans", sans-serif; font-weight: 700; }
  .seal-ribbon-text {
    top: 852px; left: 70px; transform: rotate(-28deg);
    font-family: "Roboto Condensed", sans-serif; font-weight: 700; font-size: 12px; color: var(--white); letter-spacing: 1px;
  }
</style>
</head>
<body>
<main class="flyer">
  <svg class="shapes" width="847" height="1200" viewBox="0 0 847 1200">
    <defs>
      <linearGradient id="gold-stroke" x1="0" y1="0" x2="1" y2="1">
        <stop offset="0" stop-color="#f5e2a0"/>
        <stop offset="0.5" stop-color="#b8893a"/>
        <stop offset="1" stop-color="#e9cd84"/>
      </linearGradient>
      <linearGradient id="kaaba-tones" x1="0" y1="0" x2="0" y2="1">
        <stop offset="0" stop-color="#c9bfae"/>
        <stop offset="0.35" stop-color="#3a3631"/>
        <stop offset="0.6" stop-color="#e6e3de"/>
        <stop offset="1" stop-color="#d6d2cb"/>
      </linearGradient>
      <linearGradient id="cloth-tones" x1="0" y1="0" x2="1" y2="1">
        <stop offset="0" stop-color="#a9a9a9"/>
        <stop offset="0.5" stop-color="#8a8a8a"/>
        <stop offset="1" stop-color="#b4b4b4"/>
      </linearGradient>
      <radialGradient id="seal-gold" cx="0.4" cy="0.35" r="0.7">
        <stop offset="0" stop-color="#f4cf7a"/>
        <stop offset="0.7" stop-color="#c07a1f"/>
        <stop offset="1" stop-color="#7a4410"/>
      </radialGradient>
      <clipPath id="kaaba-clip">
        <rect x="60" y="50" width="430" height="430"/>
        <rect x="60" y="50" width="430" height="430" transform="rotate(45 275 265)"/>
      </clipPath>
    </defs>

    <!-- Kaaba photo frame -->
    <g clip-path="url(#kaaba-clip)">
      <rect x="0" y="0" width="560" height="580" fill="url(#kaaba-tones)" role="img" aria-label="Photograph of the Kaaba draped in its black Kiswah surrounded by pilgrims in white"/>
    </g>
    <g fill="none" stroke="url(#gold-stroke)" stroke-width="7">
      <rect x="40" y="35" width="470" height="470" transform="rotate(45 275 270)"/>
      <rect x="75" y="75" width="420" height="420" transform="rotate(8 285 285)"/>
      <polyline points="20,520 140,620 400,620 510,520"/>
    </g>

    <!-- Kiswah cloth star -->
    <g stroke="var(--green)" stroke-width="10" fill="var(--green)">
      <rect x="545" y="185" width="245" height="245"/>
      <rect x="545" y="185" width="245" height="245" transform="rotate(45 667 307)"/>
    </g>
    <g fill="url(#cloth-tones)" role="img" aria-label="Photograph of grey silk lampas Kiswah woven with Quranic calligraphy bands">
      <rect x="545" y="185" width="245" height="245"/>
      <rect x="545" y="185" width="245" height="245" transform="rotate(45 667 307)"/>
    </g>

    <!-- Olive note stars -->
    <g fill="var(--olive)">
      <rect x="0" y="960" width="230" height="230"/>
      <rect x="0" y="960" width="230" height="230" transform="rotate(45 115 1075)"/>
      <rect x="628" y="925" width="210" height="210"/>
      <rect x="628" y="925" width="210" height="210" transform="rotate(45 733 1030)"/>
    </g>

    <!-- Guarantee seal -->
    <circle cx="107" cy="826" r="72" fill="#e8c870"/>
    <circle cx="107" cy="826" r="64" fill="url(#seal-gold)"/>
    <polygon points="60,880 170,818 178,836 68,898" fill="#d5243c"/>
  </svg>

  <p class="txt kaaba-quote">"The Kaaba is covered by an expensive black cloth which is known as 'Kiswah' which is produced and changed every year"</p>
  <p class="txt cloth-caption">"Silk lampas weave Kiswah, woven silk on a black satin ground with Quranic calligraphy, the zig-zag bands of inscription alternate with the Shahadah and the inscription, 'God, exalted be His Glory!"</p>

  <p class="txt rare">Rare</p>
  <h1 class="txt product-name">KISWAH</h1>
  <p class="txt product-sub">of the Holy Kaaba</p>
  <p class="txt product-years">(fitted in 1977 and 1982 vintage)</p>
  <h2 class="txt for-sale">For Sale</h2>

  <p class="txt seal-text"><span class="big">100%</span><span class="small">Genuine</span></p>
  <p class="txt seal-ribbon-text">GUARANTEE</p>

  <ol class="txt price-list">
    <li>1) whole piece 15 meters x 2.60 meters : £60,000</li>
    <li>2) 8 meters x 2.60 meters : £31,200</li>
    <li>3) 4 meters x 2.60 meters : £15,600</li>
    <li>4) 1 meter : £1500</li>
  </ol>

  <p class="txt cta">contact us today!<br>deals this good don't last forever.</p>
  <p class="txt email">email: relicoffer@tarnwickmail.com</p>

  <p class="txt charity-note">Please Note : A percentage of sales will go towards Sadaqah for our Muslim brothers and sisters in need around the world</p>
  <p class="txt auth-note">Hallorand's international auction house authenticity document also available to prove the Kiswah is genuine.</p>
</main>
</body>
</html>
```